Hurricane Roof Vent Blocker Postcard

Create a postcard for my company. We are a company that creates roof vent blockers that prevent water from going in the roof vent during windy weather.

I have attached a postcard that we already have that is for our customers. However, we want to sell this product to ROOFERS. So the purpose of this postcard is to make it attractive to roofers to buy and install on their customer's roof.

So the postcard should say:

"Stop unwanted callbacks for leaking roof vents. Stop wasting time going back to check leaking vents."

"Our vent blockers are permanent and can be installed on new or existing roofs"

"Installed simply from the roof top onto existing vents. No attic work."

"Simple installaton. Installed once, always protected."

"Florida-engineering uplift approved."

"Made of 26 Ga. Corvistel. Designed to last."

"Many times more effective than standard baffles."

"Maintains 100% Net Free Air requirements."

"Reduces water entry by over 99% during high wind and rain"

Universal fit - suitable for vents in the following sizes:
4-Foot Off Ridge Vents
8-Foot Off Ridge Vents
4-Inch Goose Neck Vents
6-Inch Goose Neck Vents
10-Inch Goose Neck Vents

Availabe for self-installation or professional installation.

"Suitable for flat & barrel tile roofs."

Roofing Companies who will buy the product to install it

Sans Serif

0054AA
0677BA
7BADD7
CADEEF
E8F1F8

• Pictures, QR code

```html
<!DOCTYPE html>
<html lang="en">
<head>
<meta charset="utf-8">
<title>Stormcap Vents – Roofer Postcard</title>
<link href="https://fonts.googleapis.com/css2?family=Archivo:wght@400;600;700;800;900&family=Oswald:wght@600&display=swap" rel="stylesheet">
<style>
:root{
  --navy:#0a2f6b;
  --blue:#0054AA;
  --cyan:#0aa6cc;
  --cyan-deep:#0677BA;
  --sky:#7BADD7;
  --mist:#CADEEF;
  --ice:#E8F1F8;
  --black:#050505;
  --white:#ffffff;
  --stage:#b3b3b3;
}
*{margin:0;padding:0;box-sizing:border-box}
html,body{width:1200px;height:1117px;overflow:hidden;background:var(--stage)}
body{font-family:"Archivo",Arial,sans-serif;position:relative}
.sheet{position:absolute;left:10px;top:355px;display:flex;gap:20px}
.card{position:relative;width:580px;height:407px;overflow:hidden;background:var(--white);box-shadow:0 4px 14px rgba(0,0,0,.25)}
.card-art{position:absolute;inset:0;width:100%;height:100%}
.abs{position:absolute}

.brand{display:flex;align-items:center;gap:10px}
.brand-dot{border-radius:50%;background:var(--black);flex:none}
.brand-name{font-family:"Archivo",sans-serif;font-weight:600;color:var(--black);text-align:center;line-height:1}

.front .brand{left:43px;top:21px}
.front .brand-dot{width:59px;height:59px}
.front .brand-name{font-size:28px}
.front .brand-name span{display:block;font-size:23px;margin-top:4px}

.headline{left:40px;top:124px;color:var(--white);font-weight:900;font-size:21px;line-height:22.5px;text-transform:uppercase}
.subhead{left:40px;top:193px;color:var(--white);font-weight:400;font-size:20px;line-height:20.5px;text-transform:uppercase}
.note{left:42px;top:268px;color:var(--white);font-weight:700;font-size:10.5px;line-height:13px;border-left:2px solid var(--white);padding-left:9px}

.footer{left:38px;top:356px;display:flex;align-items:center;gap:9px}
.footer-phone{display:flex;align-items:center;gap:4px;font-family:"Oswald",sans-serif;font-weight:600;font-size:27px;line-height:1;color:var(--white);letter-spacing:-.3px;white-space:nowrap}
.footer-phone .accent{color:var(--cyan)}
.footer-phone svg{flex:none}
.footer-rule{width:2px;height:30px;background:var(--cyan);flex:none}
.footer-contact{color:var(--white);font-weight:700;font-size:12.5px;line-height:16px;white-space:nowrap}
.footer-contact li{list-style:none;display:flex;align-items:center;gap:5px}
.footer-contact i{width:11px;height:11px;border-radius:50%;background:var(--cyan);display:inline-block;flex:none}

.benefits{left:34px;top:22px;width:260px;list-style:none;color:var(--white);font-weight:700;font-size:8.5px;line-height:9.5px}
.benefits li{position:relative;padding-left:12px;margin-bottom:10px}
.benefits li::before,.sizes li::before{content:"✔";position:absolute;left:0;top:0}

.back .brand{left:312px;top:23px;gap:8px}
.back .brand-dot{width:44px;height:44px}
.back .brand-name{font-size:19px}
.back .brand-name span{display:block;font-size:15px;margin-top:3px}

.postage{left:490px;top:26px;width:61px;height:62px;border:1px solid #555;font-size:6px;line-height:9.8px;text-align:center;padding-top:4px;color:var(--black)}
.address{left:384px;top:99px;width:167px;height:67px;border:1px solid #555;background:var(--white);display:flex;align-items:center;justify-content:center;font-weight:700;font-size:10px;color:var(--black)}

.fit-title{left:125px;top:187px;color:var(--white);font-weight:800;font-size:17px;line-height:1}
.fit-sub{left:125px;top:209px;color:var(--white);font-weight:700;font-size:7px}
.sizes{left:128px;top:234px;list-style:none;color:var(--white);font-size:9.5px;line-height:13.5px}
.sizes li{position:relative;padding-left:11px}

.approval{left:300px;top:325px;width:250px;height:25px;border:1.5px solid var(--cyan);color:var(--cyan);font-weight:800;font-size:13px;display:flex;align-items:center;justify-content:center}
</style>
</head>
<body>
<main class="sheet">

  <!-- FRONT -->
  <section class="card front">
    <svg class="card-art" viewBox="0 0 904 635" preserveAspectRatio="none">
      <defs>
        <linearGradient id="fCyan" x1="0" y1="0" x2="1" y2="1">
          <stop offset="0" stop-color="#14b3d8"/><stop offset="1" stop-color="#0677BA"/>
        </linearGradient>
        <linearGradient id="fDeep" x1="0" y1="0" x2="1" y2="0">
          <stop offset="0" stop-color="#0054AA"/><stop offset="1" stop-color="#0a2f6b"/>
        </linearGradient>
        <linearGradient id="familyTone" x1="0" y1="0" x2="1" y2="1">
          <stop offset="0" stop-color="#e6e6e4"/><stop offset=".55" stop-color="#8fa7c4"/><stop offset="1" stop-color="#5b5048"/>
        </linearGradient>
        <linearGradient id="mapTone" x1="0" y1="0" x2="0" y2="1">
          <stop offset="0" stop-color="#1c3a63"/><stop offset="1" stop-color="#0e2448"/>
        </linearGradient>
        <linearGradient id="leakTone" x1="0" y1="0" x2="1" y2="1">
          <stop offset="0" stop-color="#d9d2c6"/><stop offset="1" stop-color="#5a6b8a"/>
        </linearGradient>
      </defs>
      <polygon points="0,130 560,180 560,480 0,480" fill="url(#fCyan)"/>
      <polygon points="0,465 600,420 600,560 0,560" fill="url(#fDeep)"/>
      <polygon points="455,0 904,0 904,520 555,530" fill="var(--navy)"/>
      <polygon points="470,0 490,0 565,525 550,527" fill="var(--blue)"/>
      <g role="img" aria-label="Photo of a smiling family sitting on a sofa under a cardboard roof">
        <polygon points="490,0 904,0 904,318 540,318" fill="url(#familyTone)"/>
      </g>
      <polygon points="540,318 904,305 904,470 562,492" fill="var(--white)"/>
      <g role="img" aria-label="Storm track map of a hurricane approaching the southeastern coast">
        <polygon points="556,332 745,322 745,466 572,480" fill="url(#mapTone)"/>
      </g>
      <g role="img" aria-label="Photo of a man catching roof leak water in a bucket">
        <polygon points="753,320 896,314 896,460 753,466" fill="url(#leakTone)"/>
      </g>
      <polygon points="0,635 30,635 75,540 904,485 904,468 55,530 0,560" fill="var(--white)"/>
      <polygon points="30,635 904,635 904,485 75,540" fill="var(--black)"/>
    </svg>

    <div class="abs brand"><span class="brand-dot"></span><p class="brand-name">STORMCAP<span>VENTS</span></p></div>

    <h1 class="abs headline">Stop unwanted<br>callbacks for<br>leaking roof vents.</h1>
    <p class="abs subhead">Stop wasting time<br>going back to check<br>leaking vents.</p>
    <p class="abs note">Our vent blockers are permanent and<br>can be installed on new or existing roof</p>

    <div class="abs footer">
      <p class="footer-phone">
        <svg width="22" height="26" viewBox="0 0 24 24"><path d="M6.6 10.8c1.4 2.8 3.8 5.1 6.6 6.6l2.2-2.2c.3-.3.7-.4 1-.2 1.1.4 2.3.6 3.6.6.6 0 1 .4 1 1V20c0 .6-.4 1-1 1C10.6 21 3 13.4 3 4c0-.6.4-1 1-1h3.5c.6 0 1 .4 1 1 0 1.3.2 2.5.6 3.6.1.3 0 .7-.2 1L6.6 10.8z" fill="var(--cyan)"/></svg>
        <span class="accent">Call: (555)</span>&nbsp;018-4420
      </p>
      <span class="footer-rule"></span>
      <ul class="footer-contact">
        <li><i></i>Dana@StormcapVents.com</li>
        <li><i></i>www.stormcapvents.com</li>
      </ul>
    </div>
  </section>

  <!-- BACK -->
  <section class="card back">
    <svg class="card-art" viewBox="0 0 904 635" preserveAspectRatio="none">
      <defs>
        <linearGradient id="bCyan" x1="0" y1="0" x2="1" y2="1">
          <stop offset="0" stop-color="#0aa6cc"/><stop offset="1" stop-color="#0689c4"/>
        </linearGradient>
        <linearGradient id="roofTone" x1="0" y1="0" x2="0" y2="1">
          <stop offset="0" stop-color="#E8F1F8"/><stop offset=".35" stop-color="#b9cde0"/><stop offset=".55" stop-color="#6f8a5a"/><stop offset="1" stop-color="#8a9099"/>
        </linearGradient>
        <linearGradient id="trailerTone" x1="0" y1="0" x2="0" y2="1">
          <stop offset="0" stop-color="#9fb8d6"/><stop offset=".5" stop-color="#e4e8ec"/><stop offset="1" stop-color="#5f8a3e"/>
        </linearGradient>
      </defs>
      <g role="img" aria-label="Photo of a tiled residential roof with installed vent blockers under open sky">
        <polygon points="380,245 904,245 904,465 470,520" fill="url(#roofTone)"/>
      </g>
      <polygon points="0,0 455,0 400,258 0,258" fill="url(#bCyan)"/>
      <polygon points="455,0 470,0 415,260 400,258" fill="var(--blue)"/>
      <g role="img" aria-label="Photo of a branded service trailer parked on a residential street">
        <polygon points="0,245 135,245 175,520 0,520" fill="url(#trailerTone)"/>
      </g>
      <polygon points="135,245 440,258 475,520 175,520" fill="var(--navy)"/>
      <polygon points="0,635 0,555 904,455 904,475 30,600" fill="var(--cyan)"/>
      <polygon points="0,635 30,600 904,475 904,492 60,540 28,635" fill="var(--white)"/>
      <polygon points="28,635 904,635 904,492 60,540" fill="var(--black)"/>
    </svg>

    <ul class="abs benefits">
      <li>Installed simply from the roof top onto existing vents.<br>No attic work.</li>
      <li>Simple installaton. Installed once, always protected.</li>
      <li>Made of 26 Ga. Corvistel. Designed to last.</li>
      <li>Many times more effective than standard baffles.</li>
      <li>Maintains 100% Net Free Air requirements.</li>
      <li>Reduces water entry by over 99% during high<br>wind and rain.</li>
    </ul>

    <div class="abs brand"><span class="brand-dot"></span><p class="brand-name">STORMCAP<span>VENTS</span></p></div>
    <p class="abs postage">PRSRT STD<br>ECRWSS<br>U.S. Postage<br>PAID<br>EDDM RETAIL</p>
    <p class="abs address">LOCAL POSTAL CUSTOMER</p>

    <h2 class="abs fit-title">Universal fit</h2>
    <p class="abs fit-sub">suitable for vents in the following sizes:</p>
    <ul class="abs sizes">
      <li>4-Foot Off Ridge Vents</li>
      <li>8-Foot Off Ridge Vents</li>
      <li>4-Inch Goose Neck Vents</li>
      <li>6-Inch Goose Neck Vents</li>
      <li>10-Inch Goose Neck Vents</li>
    </ul>

    <p class="abs approval">Florida-engineering uplift approved.</p>

    <div class="abs footer">
      <p class="footer-phone">
        <svg width="22" height="26" viewBox="0 0 24 24"><path d="M6.6 10.8c1.4 2.8 3.8 5.1 6.6 6.6l2.2-2.2c.3-.3.7-.4 1-.2 1.1.4 2.3.6 3.6.6.6 0 1 .4 1 1V20c0 .6-.4 1-1 1C10.6 21 3 13.4 3 4c0-.6.4-1 1-1h3.5c.6 0 1 .4 1 1 0 1.3.2 2.5.6 3.6.1.3 0 .7-.2 1L6.6 10.8z" fill="var(--cyan)"/></svg>
        <span class="accent">Call: (555)</span>&nbsp;018-4420
      </p>
      <span class="footer-rule"></span>
      <ul class="footer-contact">
        <li><i></i>Dana@StormcapVents.com</li>
        <li><i></i>www.stormcapvents.com</li>
      </ul>
    </div>
  </section>

</main>
</body>
</html>
```